Logo for different Types of Exotic Salt

Dear Sirs, we are looking for a product logo for our 4 different types of Hawaiian Salt. Colours Black/white/green and yellow.
Our Brand name is "Coral Breezers". It will be packed later in a small Tube size 100-150 Gramm. . We have already made a few designs (flowers and the black one with the tiki) so that you know roughly in which direction it should go. Attached also a picture of the packaging tube. On the backside there musst be the later the Ingrediens-we dont have them yet exactly. If you have any questions, please contact me at Brandt@lanternwaves.de Best regards Lukas Brandt
Target Market(s)
Zentrovo, Retail
Industry/Entity Type
Food
Colors
Designer to choose colors to be used in the design.
Requirements
Must have
- Association for Hawaii
Nice to have
- would be nice to ad "Premium Quality" Strong associaton with Hawaii

```html
<!DOCTYPE html>
<html lang="en">
<head>
<meta charset="utf-8">
<title>Coral Breezers – Hawaii Salt Labels</title>
<link href="https://fonts.googleapis.com/css2?family=Cormorant+Garamond:wght@600;700&display=swap" rel="stylesheet">
<style>
  :root {
    --canvas: #e2f0c8;
    --pink: #e9c4da;
    --lemon: #f1e49b;
    --white: #fbfbf8;
    --green: #dde9d3;
    --black: #1d1c1e;
    --brand: #9b4565;
    --brand-red: #c9343a;
    --arc-pink: #b8708f;
    --arc-lemon: #a86a55;
    --arc-white: #a5506f;
    --arc-green: #3f9a74;
    --arc-black: #f4f1ee;
    --gold: #c7a64a;
  }
  * { margin: 0; padding: 0; box-sizing: border-box; }
  html, body {
    width: 1200px; height: 526px; overflow: hidden;
    background: var(--canvas);
  }
  .label-row {
    position: relative; width: 1200px; height: 526px;
  }
  .label {
    position: absolute; top: 95px;
    width: 190px; height: 350px;
    border-radius: 6px;
  }
  .label svg { display: block; width: 190px; height: 350px; }
  .label--pink  { left: 62px;  background: var(--pink); }
  .label--lemon { left: 295px; background: var(--lemon); }
  .label--white { left: 510px; background: var(--white); }
  .label--green { left: 722px; background: var(--green); }
  .label--black { left: 945px; background: var(--black); }

  .variety {
    font-family: "Cormorant Garamond", serif;
    font-weight: 700; font-size: 12px; letter-spacing: 2px;
  }
  .brand-name {
    font-family: "Cormorant Garamond", serif;
    font-weight: 700; font-size: 31px;
    fill: var(--brand);
  }
  .label--black .brand-name { fill: var(--brand-red); }
  .quality {
    font-family: "Cormorant Garamond", serif;
    font-weight: 700; font-size: 8.5px; letter-spacing: 1.6px;
    fill: var(--brand);
  }
  .label--black .quality { fill: var(--gold); }
  .quality-rule { stroke: var(--brand); stroke-width: 0.6; opacity: .6; }
  .label--black .quality-rule { stroke: var(--gold); }
</style>
</head>
<body>
<main class="label-row">

  <section class="label label--pink">
    <svg viewBox="0 0 190 350">
      <defs><path id="arc-pink" d="M 30,150 A 65,65 0 0 1 160,150"/></defs>
      <text class="variety" fill="var(--arc-pink)"><textPath href="#arc-pink" startOffset="50%" text-anchor="middle">PINK HAWAII SALT</textPath></text>
      <g role="img" aria-label="Red hibiscus flower with tropical leaves">
        <ellipse cx="95" cy="152" rx="58" ry="40" fill="#e0513a"/>
      </g>
      <text class="brand-name" x="95" y="232" text-anchor="middle">Coral</text>
      <text class="brand-name" x="95" y="262" text-anchor="middle">Breezers</text>
      <text class="quality" x="95" y="312" text-anchor="middle">PREMIUM QUALITY</text>
      <line class="quality-rule" x1="45" y1="320" x2="145" y2="320"/>
    </svg>
  </section>

  <section class="label label--lemon">
    <svg viewBox="0 0 190 350">
      <defs><path id="arc-lemon" d="M 30,150 A 65,65 0 0 1 160,150"/></defs>
      <text class="variety" fill="var(--arc-lemon)"><textPath href="#arc-lemon" startOffset="50%" text-anchor="middle">LEMON HAWAII SALT</textPath></text>
      <circle cx="95" cy="152" r="46" fill="#f6e56c"/>
      <g role="img" aria-label="Yellow hibiscus flower with a monstera leaf">
        <ellipse cx="95" cy="150" rx="50" ry="42" fill="#e9c23c"/>
      </g>
      <text class="brand-name" x="95" y="232" text-anchor="middle">Coral</text>
      <text class="brand-name" x="95" y="262" text-anchor="middle">Breezers</text>
      <text class="quality" x="95" y="312" text-anchor="middle">PREMIUM QUALITY</text>
      <line class="quality-rule" x1="45" y1="320" x2="145" y2="320"/>
    </svg>
  </section>

  <section class="label label--white">
    <svg viewBox="0 0 190 350">
      <defs><path id="arc-white" d="M 30,150 A 65,65 0 0 1 160,150"/></defs>
      <text class="variety" fill="var(--arc-white)"><textPath href="#arc-white" startOffset="50%" text-anchor="middle">WHITE HAWAII SALT</textPath></text>
      <circle cx="95" cy="152" r="46" fill="#f1cfc2"/>
      <g role="img" aria-label="White plumeria flower with a monstera leaf">
        <ellipse cx="95" cy="152" rx="44" ry="40" fill="#e3efe0"/>
      </g>
      <text class="brand-name" x="95" y="232" text-anchor="middle">Coral</text>
      <text class="brand-name" x="95" y="262" text-anchor="middle">Breezers</text>
      <text class="quality" x="95" y="312" text-anchor="middle">PREMIUM QUALITY</text>
      <line class="quality-rule" x1="45" y1="320" x2="145" y2="320"/>
    </svg>
  </section>

  <section class="label label--green">
    <svg viewBox="0 0 190 350">
      <defs><path id="arc-green" d="M 30,150 A 65,65 0 0 1 160,150"/></defs>
      <text class="variety" fill="var(--arc-green)"><textPath href="#arc-green" startOffset="50%" text-anchor="middle">GREEN HAWAII SALT</textPath></text>
      <circle cx="95" cy="152" r="46" fill="#c9dfa8"/>
      <g role="img" aria-label="Green monstera leaf">
        <ellipse cx="95" cy="152" rx="36" ry="40" fill="#3d9a3c"/>
      </g>
      <text class="brand-name" x="95" y="232" text-anchor="middle">Coral</text>
      <text class="brand-name" x="95" y="262" text-anchor="middle">Breezers</text>
      <text class="quality" x="95" y="312" text-anchor="middle">PREMIUM QUALITY</text>
      <line class="quality-rule" x1="45" y1="320" x2="145" y2="320"/>
    </svg>
  </section>

  <section class="label label--black">
    <svg viewBox="0 0 190 350">
      <defs>
        <path id="arc-black" d="M 30,150 A 65,65 0 0 1 160,150"/>
        <radialGradient id="black-art-tone" cx="50%" cy="50%" r="50%">
          <stop offset="0%" stop-color="#c8582e"/>
          <stop offset="100%" stop-color="#3d7f3a"/>
        </radialGradient>
      </defs>
      <text class="variety" fill="var(--arc-black)"><textPath href="#arc-black" startOffset="50%" text-anchor="middle">BLACK HAWAII SALT</textPath></text>
      <g role="img" aria-label="Illustration area: carved tiki mask in front of monstera leaves">
        <rect x="45" y="112" width="100" height="84" rx="10" fill="url(#black-art-tone)"/>
      </g>
      <text class="brand-name" x="95" y="232" text-anchor="middle">Coral</text>
      <text class="brand-name" x="95" y="262" text-anchor="middle">Breezers</text>
      <text class="quality" x="95" y="312" text-anchor="middle">PREMIUM QUALITY</text>
      <line class="quality-rule" x1="45" y1="320" x2="145" y2="320"/>
    </svg>
  </section>

</main>
</body>
</html>
```